Business Brochure / White Paper

This white paper is a marketing document to showcase ourselves to other businesses (private hospitals and other premium healthcare providers). The document should consist of bold and beautiful graphics. As an example of the sort of thing that we mean, we have attached the "velmora sky lineage records" white paper. It should consist of several A4 pages.
The content for the white paper is attached. Note that the content document is only a scaffold for the white paper and the exact layout does not need to be followed (especially text boxes which have just been placed roughly). You are free to use your artistic license to move content around in order to make the document as catchy as possible.
We have also included graphics that we have purchased licenses to and that we encourage to be used as you see fit. Note that in some places we have added a note after two asterisks (i.e. **) when we would like you to add specific images/graphics.
All of the relevant documents and graphics/images to be used to make the white paper can be found at the below link:
https://www.filquarry.net/sh/zhtwmekbb41paxl/BBDN5K3TB8FWLPNTq1tGmeOWRc?dl=0
Feel free to ask any questions.
Good Luck!
Hi,
Thank you for your submissions so far.
Please use our dropbox link for an updated and much more specific brief on what we require in terms of content, layout, and components:
Please note that we must make a decision within 3 days' time.
Please also note that we cannot select a designer unless designs for ALL PAGES of the white paper are submitted.
Thank you and good luck!

```html
<!DOCTYPE html>
<html lang="en">
<head>
<meta charset="utf-8">
<title>Helixora Business Partner White Paper</title>
<link href="https://fonts.googleapis.com/css2?family=Lato:wght@300;400;700&display=swap" rel="stylesheet">
<style>
:root{
  --bg:#c9cbcc;
  --paper:#ffffff;
  --blue:#1f5fae;
  --blue-dark:#174a8c;
  --green:#8cc63f;
  --green-title:#7bb443;
  --text:#4a4f55;
  --rule:#d5d8db;
}
*{margin:0;padding:0;box-sizing:border-box}
html,body{width:1200px;height:1027px;overflow:hidden;background:var(--bg);font-family:'Lato',sans-serif;color:var(--text)}
.page{position:absolute;width:354px;height:459px;background:var(--paper);box-shadow:0 3px 8px rgba(0,0,0,.25);overflow:hidden}
.p1{left:44px;top:38px}.p2{left:420px;top:38px}.p3{left:797px;top:38px}
.p4{left:44px;top:523px}.p5{left:420px;top:523px}.p6{left:797px;top:523px}
.topline{position:absolute;left:0;top:0;width:100%;height:3px;background:var(--green)}
.photo{position:absolute}
.brand{font-weight:400;color:var(--blue);letter-spacing:.2px}
.brand-dot{display:inline-block;border-radius:50%;background:var(--green);vertical-align:middle}
.title{position:absolute;font-weight:300;color:var(--green-title);text-transform:uppercase;letter-spacing:.2px}
.body{font-size:5.2px;line-height:6.5px;color:var(--text)}
.footer{position:absolute;left:22px;right:22px;bottom:14px;height:20px;display:flex;align-items:center;gap:10px}
.footer .brand{font-size:11px}
.footer .line{flex:1;height:2px;background:var(--rule)}
.footer .num{font-size:5.5px;color:var(--blue)}
.bullets{list-style:none;border-left:2px solid var(--blue);padding-left:10px}
.bullets li{font-size:6.2px;line-height:8px;font-weight:300;text-transform:uppercase;color:#6a7077}
.bullets li::before{content:"•";margin-right:5px;color:#6a7077}
.callout{position:absolute;border:1.5px solid var(--blue);border-radius:6px}
.col{position:absolute}
.col p{margin-bottom:5px}
/* page 1 */
.p1 .logo{position:absolute;left:52px;top:48px;font-size:26px;display:flex;align-items:center;gap:6px}
.p1 .logo .brand-dot{width:14px;height:14px}
.p1 .tag{position:absolute;left:76px;top:80px;font-size:6.4px;color:var(--green-title)}
.p1 .title{left:30px;top:292px;font-size:13.5px;line-height:19px;color:#a6d26c}
.p1 .bullets{position:absolute;left:30px;top:380px}
/* product line */
.product{position:absolute;left:26px;width:310px;display:flex;gap:10px}
.product svg{flex:none}
.product h3{font-size:6.4px;font-weight:400;color:var(--blue);margin-bottom:1px}
/* why list */
.why{position:absolute;left:20px;width:236px;list-style:none}
.why li{display:flex;align-items:center;gap:12px;height:29px;font-size:6px;line-height:7.2px;color:var(--text)}
.why svg{flex:none}
/* steps */
.steps{position:absolute;list-style:none}
.steps li{display:flex;gap:7px;margin-bottom:7px;font-size:5.2px;line-height:6.4px}
.steps b{flex:none;width:11px;height:11px;background:var(--blue);color:#fff;font-size:8px;font-weight:400;display:flex;align-items:center;justify-content:center}
</style>
</head>
<body>

<!-- Page: cover -->
<section class="page p1">
  <div class="logo"><span class="brand-dot"></span><span class="brand">helixora</span></div>
  <div class="tag">Personalised Health &amp; Wellness</div>
  <div class="photo" style="left:0;top:114px;width:354px;height:248px;background:linear-gradient(110deg,#163f70 0%,#2a5f95 45%,#7ea6cc 75%,#d7e3ef 100%)" role="img" aria-label="Doctor's hand holding a stethoscope amid floating medical icons, one reading Diagnose"></div>
  <h1 class="title">Become a<br>Helixora Business<br>Partner</h1>
  <ul class="bullets">
    <li>Cutting edge genomic &amp; precision medicine</li>
    <li>Seamless turnkey integration</li>
    <li>Lucrative new revenue stream</li>
    <li>No capital or risk involved</li>
  </ul>
</section>

<!-- Page 02: revenue -->
<section class="page p2">
  <div class="topline"></div>
  <div class="photo" style="left:0;top:8px;width:354px;height:210px;background:linear-gradient(180deg,#0c2e57 0%,#1d5c9c 55%,#6fa8dc 100%)" role="img" aria-label="Businessman silhouette facing a glowing DNA double helix"></div>
  <h2 class="title" style="left:27px;top:242px;font-size:13.5px">Lucrative New Revenue Stream</h2>
  <div class="col body" style="left:27px;top:268px;width:145px">
    <p>Genomic and precision medicine applications open a whole world of lucrative new revenue streams. Increase your businesses' revenue by hundreds to thousands of United States dollars per patient per year. Upsell to existing patients and attract new customers by offering the latest in world-class technology.</p>
    <p>HelixoraTM strategically partners with appropriate and reputable healthcare providers to enable their patients access to genomic and precision medicine services. Our partners do not invest any capital so there is no risk.</p>
  </div>
  <div class="col body" style="left:185px;top:268px;width:145px">
    <p>Partners simply stock and sell Helixora products so we only profit when they do. Patients have a variety of products on offer with varying value and corresponding price points. Helixora remains committed to ensuring that our products remain affordably accessible to the self-pay patient market and expect the same from partners.</p>
  </div>
  <div class="callout" style="left:185px;top:338px;width:146px;height:77px;padding:13px 10px">
    <p style="font-size:8.6px;line-height:12.5px;font-weight:300;color:var(--green-title)">Effortlessly increase your businesses' revenues by hundreds to thousands of US dollars per patient per year.</p>
  </div>
  <footer class="footer"><span class="brand-dot" style="width:7px;height:7px"></span><span class="brand">helixora</span><span class="line"></span><span class="num">02</span></footer>
</section>

<!-- Page 01: precision medicine -->
<section class="page p3">
  <div class="topline" style="top:18px"></div>
  <div class="photo" style="left:0;top:21px;width:354px;height:65px;background:linear-gradient(90deg,#1f5fae 0%,#1f5fae 45%,#6b98cc 75%,#c5d7ea 100%)" role="img" aria-label="Hand touching floating medical icons on a blue header"></div>
  <h2 class="title" style="left:27px;top:48px;font-size:13.5px;color:#a6d26c">Precision Medicine</h2>
  <div class="col body" style="left:26px;top:96px;width:145px">
    <p>The Larkmoor Clinic, Brightwater Hospital, Ashfield Clinic and Harbourline General Hospital. These are just some of the world's most reputable medical clinics that are already offering genomic and precision healthcare to their patients. Premium healthcare providers around the world, including private hospitals, high-end primary care practices, executive health providers and concierge medicine clinics, are rapidly following suit.</p>
    <p>Ever since the human genome was decoded, a plethora of scientific research has been compiled and the amount of new research and actionable data has grown at an exponential rate. The science has been moving much faster than industry can keep up with but precision medicine is now quickly becoming</p>
  </div>
  <div class="col body" style="left:185px;top:96px;width:145px">
    <p>mainstream practise. The revolution has begun and genomic-driven precision medicine is set to become the new standard in healthcare delivery.</p>
    <p>HelixoraTM partners with premium health providers like you to take your business to the next level and set you apart from competitors. Our cutting-edge products allow you to offer the same in world-class precision and genomic healthcare. The science is clear, the technology is ready, and the time for clinical implementation is now.</p>
  </div>
  <ul class="bullets" style="position:absolute;left:26px;top:234px">
    <li>Improve patient care</li>
    <li>Increase therapy effectiveness</li>
    <li>Limit adverse outcomes</li>
    <li>Improve medical compliance</li>
    <li>Improve economic efficieny</li>
  </ul>
  <div class="callout" style="left:210px;top:230px;width:118px;height:93px;padding:16px 10px 0">
    <p style="font-size:9px;font-weight:300;color:var(--green-title);margin-bottom:5px">DID YOU KNOW?</p>
    <p class="body" style="font-size:5px;line-height:6.2px">Response rates for many prescribed drugs are as low as 50% and that genetic factors can account for up to 95% of drug-response variability and susceptibility!2,3 That's why physicians are turning to precision prescribing!</p>
  </div>
  <svg style="position:absolute;left:261px;top:213px" width="24" height="24" viewBox="0 0 24 24"><circle cx="12" cy="12" r="11" fill="var(--green)"/><circle cx="12" cy="10" r="4" fill="#fff"/><rect x="10" y="14" width="4" height="3" fill="#fff"/></svg>
  <svg style="position:absolute;left:30px;top:333px" width="14" height="10" viewBox="0 0 14 10"><path d="M0 10V5L3 0h2L3 5h2v5zM8 10V5l3-5h2l-2 5h2v5z" fill="#c4c8cc"/></svg>
  <div class="col body" style="left:30px;top:348px;width:290px;font-size:5px;line-height:6.2px">Doctors have always recognized that every patient is unique, and doctors have always tried to tailor their treatments as best they can to individuals. You can match a blood transfusion to a blood type — that was an important discovery. What if matching a cancer cure to our genetic code was just as easy, just as standard? What if figuring out the right dose of medicine was as simple as taking our temperature?</div>
  <svg style="position:absolute;left:319px;top:370px" width="14" height="10" viewBox="0 0 14 10"><path d="M0 0v5h2L0 10h2l3-5V0zM8 0v5h2l-2 5h2l3-5V0z" fill="#c4c8cc"/></svg>
  <div class="body" style="position:absolute;right:27px;top:384px;text-align:right;font-size:5px;line-height:6px">- <span style="color:var(--blue)">President Harlan Whitcombe</span>, at the announcement of a $215 Million<br>Precision-Medicine Genetic Plan, January 30, 2015.1</div>
  <footer class="footer"><span class="brand-dot" style="width:7px;height:7px"></span><span class="brand">helixora</span><span class="line"></span><span class="num">01</span></footer>
</section>

<!-- Page 03: product line -->
<section class="page p4">
  <div class="topline" style="top:18px"></div>
  <div class="photo" style="left:0;top:21px;width:354px;height:62px;background:linear-gradient(90deg,#1f5fae 0%,#2a6bb8 40%,#7fa4cf 75%,#b9cde4 100%)" role="img" aria-label="Scientists working in a laboratory"></div>
  <h2 class="title" style="left:27px;top:46px;font-size:13.5px;color:#a6d26c">Product Line</h2>
  <div class="product" style="top:102px">
    <svg width="22" height="22" viewBox="0 0 22 22"><path d="M4 18C10 14 12 8 18 4M4 4c6 4 8 10 14 14" stroke="var(--green)" stroke-width="2" fill="none"/></svg>
    <div><h3>Whole Genome Sequencing</h3><p class="body">The human genome was first decoded in 2003, taking over 13 years and $2.7 billion to complete.4 Thanks to exponential advances in technology, helixoraTM can now do the same at only a fraction of the time and cost. Whole Genome Sequencing (WGS) provides a complete analysis of your patients' DNA and future proofs them so that dynamic updates can be generated as scientific discovery continues at its rapid pace.</p></div>
  </div>
  <div class="product" style="top:157px">
    <svg width="22" height="22" viewBox="0 0 22 22"><circle cx="7" cy="7" r="5" stroke="var(--green)" stroke-width="1.8" fill="none"/><circle cx="15" cy="7" r="5" stroke="var(--green)" stroke-width="1.8" fill="none"/><circle cx="7" cy="15" r="5" stroke="var(--green)" stroke-width="1.8" fill="none"/><circle cx="15" cy="15" r="5" stroke="var(--green)" stroke-width="1.8" fill="none"/></svg>
    <div><h3>Whole Exome Sequencing</h3><p class="body">The "exome" is the known gene coding region of an individual's entire genome. In other words, it is where the real action takes place. Whole exome sequencing will provide most of the important answers that patients and physicians are seeking. Whole exome sequencing can therefore be considered to be more efficient, but less thorough, than whole genome sequencing.</p></div>
  </div>
  <div class="product" style="top:212px">
    <svg width="22" height="22" viewBox="0 0 22 22"><path d="M3 18l6-7 4 4 6-10" stroke="var(--green)" stroke-width="2" fill="none"/><circle cx="3" cy="18" r="2" fill="var(--green)"/><circle cx="9" cy="11" r="2" fill="var(--green)"/><circle cx="13" cy="15" r="2" fill="var(--green)"/><circle cx="19" cy="5" r="2" fill="var(--green)"/></svg>
    <div><h3>Disease Risk Genotyping</h3><p class="body">Prevention is always better than cure. Scientific research is moving at rapid speed and numerous genes have already been associated with a range of diseases, including cancers, heart conditions and diabetes. There are over 7,500 known inherited diseases affecting millions of individuals worldwide. In many cases, early recognition and management will significantly improve these individuals' quality and length of life.</p></div>
  </div>
  <div class="product" style="top:267px">
    <svg width="22" height="22" viewBox="0 0 22 22"><rect x="3" y="8" width="16" height="7" rx="3.5" transform="rotate(-45 11 11)" fill="var(--green)"/><circle cx="17" cy="17" r="3" fill="var(--green)"/></svg>
    <div><h3>Pharmacogenomic Genotyping</h3><p class="body">Scientific research has shown that the response rate for many prescribed drugs is as low as 50% and that genetic factors can account for up to 95% of drug-response variability and susceptibility!2,3 In other words, many of the billions of drugs prescribed every year are inadequately dosed, leading to side effects or no effects at all. This is why physicians around the world are turning to "precision prescribing". Pharmacogenomic testing allows for the proactive identification of appropriate drugs and dosages for a range of commonly prescribed and over-the-counter medications. In fact, several studies have shown that over 74% of people taking a genetic test for medication compatibility learned information that is relevant to them.5-8</p></div>
  </div>
  <div class="product" style="top:350px">
    <svg width="22" height="22" viewBox="0 0 22 22"><path d="M8 3h5v4h-3v3l5 3-4 7H7l2-4-3-3V7h2z" fill="var(--green)"/></svg>
    <div><h3>Other Genotyping Products</h3><p class="body">An ever-growing number of tests are available depending on the specific needs and desires of your business. Microbiome, dietary, and family planning tests are just some examples to name a few.</p></div>
  </div>
  <footer class="footer"><span class="brand-dot" style="width:7px;height:7px"></span><span class="brand">helixora</span><span class="line"></span><span class="num">03</span></footer>
</section>

<!-- Page 04: why -->
<section class="page p5">
  <div class="photo" style="left:0;top:0;width:354px;height:459px;background:linear-gradient(180deg,#b7bec7 0%,#dfe3e8 40%,#eef0f2 70%,#a9b0b9 100%)" role="img" aria-label="Bright modern genetic laboratory with equipment"></div>
  <div style="position:absolute;left:50px;top:43px;width:266px;height:352px;background:#fff"></div>
  <div style="position:absolute;left:63px;top:33px;width:164px;height:41px;background:var(--blue)"></div>
  <h2 class="title" style="left:84px;top:47px;font-size:13.5px;color:#a6d26c">Why Helixora?</h2>
  <ul class="why" style="left:70px;top:87px">
    <li><svg width="14" height="14" viewBox="0 0 14 14"><path d="M3 1h8v4a4 4 0 0 1-8 0zM6 9h2v2h2v2H4v-2h2z" fill="var(--green)"/></svg>Industry leading partnerships with some of the most reputable names in healthcare &amp; life sciences</li>
    <li><svg width="14" height="14" viewBox="0 0 14 14"><circle cx="7" cy="6" r="5" fill="none" stroke="var(--green)" stroke-width="1.8"/><path d="M4 10l-1 4 4-2 4 2-1-4" fill="var(--green)"/></svg>Physician created clinical-grade quality</li>
    <li><svg width="14" height="14" viewBox="0 0 14 14"><rect x="2.5" y="1.5" width="9" height="11" fill="none" stroke="var(--green)" stroke-width="1.5"/><path d="M4.5 5h5M4.5 7.5h5M4.5 10h3" stroke="var(--green)"/></svg>HRA cleared genetic testing kits</li>
    <li><svg width="14" height="14" viewBox="0 0 14 14"><path d="M5 1h4v3H7v2l4 3-3 5H4l2-4-3-3V4h2z" fill="var(--green)"/></svg>Top-tier laboratories – CLRA-certified and/or PAL/NALT/ ISO15189-accredited</li>
    <li><svg width="14" height="14" viewBox="0 0 14 14"><circle cx="7" cy="7" r="5.5" fill="none" stroke="var(--green)" stroke-width="1.5"/><path d="M4.5 7l2 2 3-4" stroke="var(--green)" stroke-width="1.5" fill="none"/></svg>Key-turn solution covering everything from A to Z.</li>
    <li><svg width="14" height="14" viewBox="0 0 14 14"><circle cx="7" cy="7" r="4" fill="none" stroke="var(--green)" stroke-width="3" stroke-dasharray="2.5 1.6"/></svg>Seamless integration into your existing business</li>
    <li><svg width="14" height="14" viewBox="0 0 14 14"><path d="M2 6h3v7H2zM6 6l3-5 1 1-1 4h3l-1 7H6z" fill="var(--green)"/></svg>Rapidly adaptive thanks to our comprehensive market oversight</li>
    <li><svg width="14" height="14" viewBox="0 0 14 14"><path d="M1 6l4-2 3 2 3-2 2 2-5 4z" fill="var(--green)"/></svg>Bespoke partnerships based on your unique needs</li>
    <li><svg width="14" height="14" viewBox="0 0 14 14"><circle cx="7" cy="7" r="6" fill="var(--green)"/><circle cx="7" cy="7" r="3" fill="#fff"/></svg>New Zealand gold stamp – consistently rated by Clearwater Integrity Index as one of the least corrupt and best places to do business in the world.</li>
  </ul>
  <footer class="footer"><span class="brand-dot" style="width:7px;height:7px"></span><span class="brand">helixora</span><span class="line" style="background:transparent"></span><span class="num" style="color:#fff">04</span></footer>
</section>

<!-- Page 05: partnership -->
<section class="page p6">
  <div class="topline" style="top:5px"></div>
  <div class="photo" style="left:14px;top:28px;width:326px;height:74px;background:linear-gradient(180deg,#f2f4f7 0%,#7e9ab8 45%,#2f4f7a 100%)" role="img" aria-label="Group of doctors, nurses and surgeons standing in a row"></div>
  <h2 class="title" style="left:27px;top:111px;font-size:13px">What a partnership with Helixora looks like</h2>
  <ol class="steps" style="left:30px;top:140px;width:150px">
    <li><b>1</b><span>Helixora delivers genetic testing kits and marketing material for your business to stock.</span></li>
    <li><b>2</b><span>Your patient purchases a Helixora Product</span></li>
    <li><b>3</b><span>A simple cheek swab or saliva sample is collected from your patient – this takes less than a minute.</span></li>
    <li><b>4</b><span>Details of the patient and kit are entered into your businesses' online Helixora portal – this takes less than 5 minutes.</span></li>
  </ol>
  <ol class="steps" style="left:195px;top:140px;width:140px">
    <li><b>5</b><span>Sample is collected from your business premises.</span></li>
    <li><b>6</b><span>Sample undergoes DNA extraction, testing and analysis.</span></li>
    <li><b>7</b><span>Clinically actionable reports are delivered to you several weeks later.</span></li>
  </ol>
  <div class="photo" style="left:20px;top:250px;width:155px;height:148px;background:linear-gradient(135deg,#1d6e6a 0%,#2d8f86 50%,#e8eef2 100%)" role="img" aria-label="Open brochure and booklet mockups"></div>
  <div class="photo" style="left:170px;top:242px;width:80px;height:62px;background:linear-gradient(135deg,#ffffff 0%,#e3e8ee 100%)" role="img" aria-label="White genetic testing kit box"></div>
  <div class="photo" style="left:266px;top:245px;width:34px;height:160px;background:linear-gradient(90deg,#c9ced3 0%,#eef1f3 50%,#b7bcc2 100%)" role="img" aria-label="Brochure display stand"></div>
  <footer class="footer"><span class="brand-dot" style="width:7px;height:7px"></span><span class="brand">helixora</span><span class="line"></span><span class="num">05</span></footer>
</section>

</body>
</html>
```